Business Card Design

We need a business card designed for a new company based in Melbourne called Korvum solutions. Korvum solutions provides management consulting specialising in the health and social services sector.

Korvum solutions offer a unique set of specialist skills │dealing with all levels of government │ unique communication skills│intimate knowledge of the health sector │solutions tailored to unique circumstances.

Korvum solutions takes on a select number of clients at any one time, this ensures that your organisation receives the attention required. On larger projects, Korvum solutions join up with other consultants to bring specialist skills to a project.
Updates

This is the first time I have used Pixel Bazaar and thank you all for responding. The variation is amazing and makes it hard to decide. I have to ask some of my friends to give me their views. The response is fantastic. The one I pick will basically be the most visually appealing

Industry/Entity Type

Management Consulting

Contact Information for Business Card

Marcus Pellow, Principal, Korvum solutions, 14 Wexcombe Ave, Dunlarry VIC 3999, 0400 137 284, marcusp@korvumsolutions.example, www.korvumsolutions.example

```html
<!DOCTYPE html>
<html lang="en">
<head>
<meta charset="utf-8">
<title>Korvum solutions – Business Card</title>
<link href="https://fonts.googleapis.com/css2?family=Lato:wght@400;700;900&display=swap" rel="stylesheet">
<style>
  :root {
    --backdrop: #2b2b2d;
    --brand-red: #c3162c;
    --brand-red-deep: #a50f22;
    --card-white: #f4f4f4;
    --band-grey: #d9d9d9;
    --ink: #1c1c1c;
    --white: #ffffff;
  }
  * { margin: 0; padding: 0; box-sizing: border-box; }
  html, body {
    width: 1200px; height: 900px; overflow: hidden;
    background: var(--backdrop);
    font-family: "Lato", Arial, sans-serif;
  }
  .card {
    position: absolute; left: 100px; top: 145px;
    width: 1000px; height: 610px;
    background: var(--card-white);
    box-shadow: 0 20px 50px rgba(0,0,0,.55);
    overflow: hidden;
  }
  .card-backdrop { position: absolute; inset: 0; }
  .pattern-area { position: absolute; }
  .pattern-area--left { left: 18px; top: 200px; width: 90px; height: 120px; }
  .pattern-area--center { left: 480px; top: 60px; width: 40px; height: 130px; }

  .brand { position: absolute; left: 140px; top: 150px; color: var(--white); }
  .brand-holder { font-size: 19px; color: var(--ink); letter-spacing: 1px; margin-bottom: 4px; }
  .brand-name { font-size: 46px; font-weight: 700; line-height: 1; letter-spacing: 1px; }
  .brand-tagline { font-size: 11px; font-weight: 700; letter-spacing: 1.5px; margin-top: 8px; text-transform: uppercase; }

  .person { position: absolute; right: 60px; top: 95px; text-align: right; }
  .person-name { font-size: 30px; font-weight: 900; color: var(--white); letter-spacing: .5px; text-transform: uppercase; }
  .person-role { font-size: 17px; font-weight: 900; color: var(--ink); letter-spacing: 1px; text-transform: uppercase; }

  .strengths {
    position: absolute; left: 50px; top: 360px; list-style: none;
    color: var(--brand-red); font-weight: 900; font-size: 24px; line-height: 1.2;
  }
  .strengths li { padding-left: 16px; text-indent: -16px; }
  .strengths li::before { content: "- "; }

  .contact { position: absolute; left: 560px; top: 335px; list-style: none; }
  .contact li { display: flex; align-items: center; gap: 14px; height: 46px; font-size: 21px; font-weight: 700; color: var(--ink); }
  .contact-icon { width: 34px; height: 34px; border-radius: 7px; background: var(--brand-red); flex: none; }
</style>
</head>
<body>
  <article class="card">
    <svg class="card-backdrop" width="1000" height="610" viewBox="0 0 1000 610" aria-hidden="true">
      <defs>
        <linearGradient id="redFill" x1="0" y1="0" x2="1" y2="1">
          <stop offset="0" stop-color="#cf1b31"/>
          <stop offset="1" stop-color="#a50f22"/>
        </linearGradient>
      </defs>
      <rect width="1000" height="610" fill="url(#redFill)"/>
      <path d="M0 330 C220 250 420 300 600 340 C760 375 900 300 1000 250 L1000 610 L0 610 Z" fill="var(--band-grey)"/>
      <path d="M0 350 C220 275 420 320 600 360 C760 395 900 325 1000 275 L1000 610 L0 610 Z" fill="var(--card-white)"/>
    </svg>

    <div class="pattern-area pattern-area--left" role="img" aria-label="Faint grid of plus-sign decoration" style="background:rgba(255,255,255,.08)"></div>
    <div class="pattern-area pattern-area--center" role="img" aria-label="Vertical row of plus-sign decoration" style="background:rgba(0,0,0,.06)"></div>

    <div class="brand">
      <p class="brand-holder">Marcus Pellow</p>
      <p class="brand-name">Korvum solutions</p>
      <p class="brand-tagline">Health &amp; Social Services Consulting</p>
    </div>

    <div class="person">
      <p class="person-name">Marcus Pellow</p>
      <p class="person-role">Principal</p>
    </div>

    <ul class="strengths">
      <li>Dealing with all levels of government</li>
      <li>Unique communication skills</li>
      <li>Intimate knowledge of the health sector</li>
      <li>Solutions tailored to unique circumstances.</li>
    </ul>

    <ul class="contact">
      <li>
        <svg class="contact-icon" viewBox="0 0 34 34" aria-hidden="true"><rect width="34" height="34" rx="7" fill="var(--brand-red)"/><path d="M8 13 Q17 6 26 13 L23 16 L20 13 L14 13 L11 16 Z M11 17 H23 V26 H11 Z" fill="#fff"/></svg>
        <span>0400 137 284</span>
      </li>
      <li>
        <svg class="contact-icon" viewBox="0 0 34 34" aria-hidden="true"><rect width="34" height="34" rx="7" fill="var(--brand-red)"/><rect x="7" y="10" width="20" height="14" fill="none" stroke="#fff" stroke-width="2"/><path d="M7 10 L17 18 L27 10" fill="none" stroke="#fff" stroke-width="2"/></svg>
        <span>marcusp@korvumsolutions.example</span>
      </li>
      <li>
        <svg class="contact-icon" viewBox="0 0 34 34" aria-hidden="true"><rect width="34" height="34" rx="7" fill="var(--brand-red)"/><circle cx="17" cy="17" r="10" fill="none" stroke="#fff" stroke-width="2"/><path d="M7 17 H27 M17 7 Q11 17 17 27 M17 7 Q23 17 17 27" fill="none" stroke="#fff" stroke-width="1.6"/></svg>
        <span>www.korvumsolutions.example</span>
      </li>
      <li>
        <svg class="contact-icon" viewBox="0 0 34 34" aria-hidden="true"><rect width="34" height="34" rx="7" fill="var(--brand-red)"/><path d="M17 28 C11 20 10 17 10 14 A7 7 0 0 1 24 14 C24 17 23 20 17 28 Z" fill="#fff"/><circle cx="17" cy="14" r="3" fill="var(--brand-red)"/></svg>
        <span>14 Wexcombe Ave, Dunlarry VIC 3999</span>
      </li>
    </ul>
  </article>
</body>
</html>
```